Verno Care is an innovative Australian Business offering organisations an online solution for depre

We need an extremely professional Business card that is positive as we offer engaging online technology to help with depression. Our target market is large scale adoption by major Organisations.The logo is supplied but font can alter .

We would like to see designs that use our logo on the front with altered font . Open to alteration on the sphere concept for the logo but happy with this and you may alter slightly if you wish.

back -displays contact details, with our names coloured in orange like the orange on our site . use creative flair

initial names to appear on cards are Sam Pelling Director 0452316078 Sa.Pellingg@verno-care.com.au, www.verno-care.com.au

We are looking for fresh and professional designs with some creative flair.

i have attached a mock up of our site that should come across in the business card design...but
No images required from site

business card dimensions are 54x89. we will print logo in high gloss and card will be matt.

Target Market(s)

Large adoption by Doctors , Universities , not for profits and large organisations

Industry/Entity Type

Business

Requirements
Must have
• linkage to our site by way of design but no images needed from site except logo

Needs to be bright and vibrant in design as online tools for depression and anxiety . Also professional look.

```html
<!DOCTYPE html>
<html lang="en">
<head>
<meta charset="utf-8">
<title>Verno Care – Business Card</title>
<link rel="stylesheet" href="https://fonts.googleapis.com/css2?family=Didact+Gothic&family=Open+Sans:wght@400;600&display=swap">
<style>
  :root {
    --bg: #e6e7e9;
    --card: #ffffff;
    --card-shade: #eeeeef;
    --orange: #ff5414;
    --green: #2f8a45;
    --ink: #151515;
    --panel: #111111;
    --panel-text: #f2f2f2;
    --mosaic: #e2e2e4;
  }
  * { box-sizing: border-box; margin: 0; padding: 0; }
  html, body { width: 1200px; height: 1000px; overflow: hidden; }
  body {
    background: var(--bg);
    display: flex;
    flex-direction: column;
    align-items: center;
    justify-content: center;
    gap: 56px;
  }
  .card {
    position: relative;
    width: 640px;
    height: 388px;
    border-radius: 14px;
    overflow: hidden;
    background: linear-gradient(160deg, var(--card) 0%, var(--card) 55%, var(--card-shade) 100%);
    box-shadow: 0 10px 30px rgba(0,0,0,.14);
  }
  /* Front */
  .brand-name {
    position: absolute;
    left: 150px;
    top: 118px;
    font-family: "Didact Gothic", "Century Gothic", sans-serif;
    font-size: 54px;
    line-height: 1;
    color: var(--ink);
    letter-spacing: 1px;
    white-space: nowrap;
  }
  .front-band {
    position: absolute;
    left: 0; top: 262px;
    width: 470px; height: 46px;
    background: var(--orange);
  }
  /* Back */
  .back-tab {
    position: absolute;
    left: 36px; top: 0;
    width: 184px; height: 40px;
    background: var(--orange);
  }
  .holder {
    position: absolute;
    left: 36px; top: 68px;
    font-family: "Open Sans", sans-serif;
    color: var(--green);
    white-space: nowrap;
  }
  .holder-name { font-size: 34px; font-weight: 600; line-height: 1.1; }
  .holder-role { font-size: 17px; font-weight: 600; margin-top: 2px; }
  .back-block {
    position: absolute;
    left: 36px; top: 176px;
    width: 184px; height: 212px;
    background: var(--orange);
  }
  .contact-panel {
    position: absolute;
    left: 14px; top: 226px;
    width: 270px; height: 120px;
    background: var(--panel);
    padding: 16px 14px;
    display: flex;
    flex-direction: column;
    gap: 10px;
    font-family: "Open Sans", sans-serif;
    font-size: 13px;
    color: var(--panel-text);
    white-space: nowrap;
  }
  .contact-line { display: flex; align-items: center; gap: 10px; }
  .contact-icon { width: 14px; height: 14px; flex: none; }
  .contact-at { width: 14px; text-align: center; font-size: 13px; flex: none; }
  .mosaic-area {
    position: absolute;
    left: 330px; top: 150px;
    width: 180px; height: 170px;
    background: linear-gradient(180deg, var(--mosaic) 0%, rgba(226,226,228,0.35) 100%);
  }
</style>
</head>
<body>
  <section class="card card-front" aria-label="Card front">
    <span class="brand-name">Verno Care</span>
    <div class="front-band"></div>
  </section>

  <section class="card card-back" aria-label="Card back">
    <div class="back-tab"></div>
    <div class="holder">
      <p class="holder-name">Sam Pelling</p>
      <p class="holder-role">Director</p>
    </div>
    <div class="mosaic-area" role="img" aria-label="Faint grey square mosaic decoration"></div>
    <div class="back-block"></div>
    <div class="contact-panel">
      <p class="contact-line">
        <svg class="contact-icon" viewBox="0 0 16 16" aria-hidden="true"><path fill="#f2f2f2" d="M1 5c0-2 3-3 7-3s7 1 7 3v1h-4V5H5v1H1zM3 8l2-2h6l2 2v6H3zm5 1.5a2 2 0 100 4 2 2 0 000-4z"/></svg>
        <span>0452316078</span>
      </p>
      <p class="contact-line">
        <span class="contact-at">@</span>
        <span>Sa.Pellingg@verno-care.com.au</span>
      </p>
      <p class="contact-line">
        <svg class="contact-icon" viewBox="0 0 16 16" aria-hidden="true"><rect x="1.5" y="2.5" width="13" height="9" fill="none" stroke="#f2f2f2" stroke-width="1.4"/><rect x="6" y="12" width="4" height="1.5" fill="#f2f2f2"/><rect x="4" y="13.5" width="8" height="1.2" fill="#f2f2f2"/></svg>
        <span>www.verno-care.com.au</span>
      </p>
    </div>
  </section>
</body>
</html>
```